Professional business cards for real estate development company

I need business cards for my new real estate development company. The company, "KORVA" is a real estate development, investment, and advisory firm with a focus on multifamily, office, and mixed-use projects across primary and secondary markets in the Southeast United States.

Style preference is modern

Industry/Entity Type

Real Estate Development

Contact Information for Business Card

The business cards need to include:
Name
Title
Mailing Address
Phone Number
Web Address

Logo is attached. I would like white to be the primary color with incorporation of the company colors: #232D3A and #B5A451

Font styles to use
Other font styles liked:
• Montserrat, Avenir

Requirements
Must have
• Company Logo. No need to include the company name since the name is in the logo.
Should not have
• No line type designs

```html
<!DOCTYPE html>
<html lang="en">
<head>
<meta charset="utf-8">
<title>KORVA Business Card</title>
<link href="https://fonts.googleapis.com/css2?family=Montserrat:wght@300;400;500&display=swap" rel="stylesheet">
<style>
  :root {
    --backdrop: #1c1c1e;
    --gold: #b5a451;
    --navy: #232d3a;
    --ink: #1a1e24;
  }
  * { margin: 0; padding: 0; box-sizing: border-box; }
  html, body {
    width: 1200px;
    height: 800px;
    overflow: hidden;
    background: var(--backdrop);
  }
  .sheet {
    width: 1200px;
    height: 800px;
    display: flex;
    align-items: center;
    justify-content: center;
    gap: 50px;
  }
  .card {
    width: 540px;
    height: 310px;
    border-radius: 20px;
    position: relative;
    font-family: 'Montserrat', sans-serif;
  }
  .card-front {
    background: var(--gold);
    color: var(--ink);
  }
  .card-back {
    background: var(--navy);
    display: flex;
    align-items: center;
    justify-content: center;
  }
  .identity {
    position: absolute;
    top: 58px;
    right: 40px;
    text-align: right;
  }
  .identity-name {
    font-weight: 300;
    font-size: 27px;
    letter-spacing: 1px;
    text-transform: uppercase;
  }
  .identity-title {
    font-weight: 300;
    font-size: 16px;
    letter-spacing: 1.5px;
    text-transform: uppercase;
    margin-top: 4px;
  }
  .contact {
    position: absolute;
    left: 40px;
    bottom: 48px;
    list-style: none;
    font-weight: 300;
    font-size: 17px;
    line-height: 1.5;
  }
  .brand {
    display: flex;
    align-items: center;
    gap: 14px;
  }
  .brand-square {
    width: 26px;
    height: 26px;
    background: var(--gold);
  }
  .brand-name {
    color: var(--gold);
    font-weight: 400;
    font-size: 52px;
    letter-spacing: 4px;
  }
</style>
</head>
<body>
  <main class="sheet">
    <section class="card card-front">
      <div class="identity">
        <p class="identity-name">Daniel Rowe</p>
        <p class="identity-title">Partner</p>
      </div>
      <ul class="contact">
        <li>T: +1-404-555-0182</li>
        <li>E: danielr@korvadevelopment.com</li>
        <li>W: korvadevelopment.com</li>
      </ul>
    </section>
    <section class="card card-back">
      <div class="brand">
        <span class="brand-square"></span>
        <span class="brand-name">KORVA</span>
      </div>
    </section>
  </main>
</body>
</html>
```